Professional Business Card for Commercial Cleaning Company

We need a business card that represents our commercial janitorial cleaning company and represent several brands for our company so we do not want to highlight the logo too much. We want something that says we are professional.
Notes:No website or address as we have many locations and many websites and companies under our corporate name of "Brightmere Holdings, LLC" . Every time we hand a customer a business card they have contacted us via another brand we own but we don't want to have 21 business cards so we want to not focus on Brightmere Holdings, LLC too much since people will automatically ask "What is Brightmere Holdings, LLC" Example: Noodle Barn and Wrap Lodge restaurants are owned by "Zest! Brands" is the corporation name. Same principle here. Except we do not advertise at this time that all of our brands are connected. Hope this helps.
Target Market(s)
Commercial Cleaning
Industry/Entity Type
Janitorial Service
Contact Information for Business Card
Miles Penrow
Business Development
482-639-2274
sales@brightmereholdingsllc.example
Requirements
Must have
- Logo with contact information, need to be able to easily edit contact info for others in my office.
Nice to have
- Professional Image. Like to see a colorful bold look and a more standard business card look.
Should not have
- Any type of cleaning icons, tools, people or water.

```html
<!DOCTYPE html>
<html lang="en">
<head>
<meta charset="utf-8">
<title>Brightmere Holdings, LLC — Business Card</title>
<link href="https://fonts.googleapis.com/css2?family=Roboto:wght@500&family=Work+Sans:wght@400;600&display=swap" rel="stylesheet">
<style>
  :root {
    --navy: #1c3d75;
    --green: #69a843;
    --white: #ffffff;
    --backdrop: #e9e6e1;
    --shadow: rgba(40, 30, 20, 0.25);
  }
  * { box-sizing: border-box; margin: 0; padding: 0; }
  html, body {
    width: 1200px; height: 930px; overflow: hidden;
    background: var(--backdrop);
    font-family: "Work Sans", sans-serif;
  }
  .canvas { position: relative; width: 1200px; height: 930px; }
  .card {
    position: absolute; left: 318px; width: 564px; height: 323px;
    border-radius: 26px; overflow: hidden;
    box-shadow: 0 6px 16px var(--shadow);
  }
  .card--front { top: 125px; background: var(--white); }
  .card--back { top: 514px; background: var(--navy); }
  .front-curve { position: absolute; inset: 0; width: 100%; height: 100%; }
  .brand-name {
    font-family: "Work Sans", sans-serif;
    font-weight: 600; letter-spacing: -0.2px; white-space: nowrap;
  }
  .card--front .brand-name {
    position: absolute; left: 30px; top: 50px;
    font-size: 22px; color: var(--navy);
  }
  .card--back .brand-name {
    position: absolute; left: 0; right: 0; top: 158px;
    text-align: center; font-size: 20px; color: var(--white);
  }
  .details {
    position: absolute; right: 26px; top: 138px;
    text-align: right; color: var(--white);
  }
  .person-name {
    font-family: "Roboto", sans-serif; font-weight: 500;
    font-size: 26px; line-height: 1; letter-spacing: 0.2px;
  }
  .person-role { font-size: 13px; margin-top: 6px; letter-spacing: 0.3px; }
  .contact { list-style: none; margin-top: 22px; font-size: 13px; line-height: 20px; letter-spacing: 0.3px; }
  .contact li { display: flex; justify-content: flex-end; align-items: center; gap: 7px; margin-right: -1px; }
  .contact svg { width: 9px; height: 9px; flex: none; }
</style>
</head>
<body>
<main class="canvas">
  <section class="card card--front" aria-label="Business card front">
    <svg class="front-curve" viewBox="0 0 564 323" preserveAspectRatio="none" aria-hidden="true">
      <path d="M82 323 Q250 104 564 97 L564 323 Z" fill="var(--green)"/>
      <path d="M111 323 Q268 118 564 100 L564 323 Z" fill="var(--navy)"/>
    </svg>
    <p class="brand-name">Brightmere Holdings, LLC</p>
    <div class="details">
      <h1 class="person-name">MILES PENROW</h1>
      <p class="person-role">Business Development</p>
      <ul class="contact">
        <li>482-639-2274
          <svg viewBox="0 0 10 10" aria-hidden="true"><path d="M2 1 L4 1 L4.6 3 L3.4 4 Q4.5 6 6 6.6 L7 5.4 L9 6 L9 8 Q8.5 9 7 9 Q1 8 1 3 Q1 1.5 2 1 Z" fill="var(--white)"/></svg>
        </li>
        <li>sales@brightmereholdingsllc.example
          <svg viewBox="0 0 10 10" aria-hidden="true"><rect x="1" y="2.5" width="8" height="5.5" rx="0.6" fill="none" stroke="var(--white)" stroke-width="1.1"/><path d="M1.3 3 L5 5.6 L8.7 3" fill="none" stroke="var(--white)" stroke-width="1"/></svg>
        </li>
      </ul>
    </div>
  </section>

  <section class="card card--back" aria-label="Business card back">
    <p class="brand-name">Brightmere Holdings, LLC</p>
  </section>
</main>
</body>
</html>
```